Luxury Business Card Design for Velvet Coach

I need a high-end, luxury business card design for my premium limo service, Velvet Coach. The card should reflect elegance and exclusivity, using a black and gold color scheme with a minimalist and sophisticated layout. The design should include:

Target Market(s)

High-end clients, corporate executives, luxury travelers, VIPs, and celebrities looking for premium limousine and chauffeur services

Industry/Entity Type

Limo

Contact Information for Business Card

Cluttered design—should be sleek & minimal

Font styles to use
Other font styles liked:
• CINZEL DECORATIVE

Requirements
Must have
• 📞 416-383-RIDE (416-383-7433) 📞 Toll-Free: 1 (888) 294-RIDE (7433) Email: book@velvet-coach.com
Nice to have
• QR Code , I need a high-end, luxury business card design for my premium limo service, Velvet Coach. The card should reflect elegance and exclusivity, using a black and gold color scheme with a minimalist and sophisticated layout. It should align with the branding, luxury feel, and premium aesthetics seen on our website www.velvet-coach.com.

```html
<!DOCTYPE html>
<html lang="en">
<head>
<meta charset="utf-8">
<title>Velvet Coach – Business Card</title>
<link href="https://fonts.googleapis.com/css2?family=Cinzel:wght@600;700&family=Montserrat:wght@400;500&display=swap" rel="stylesheet">
<style>
  :root {
    --backdrop: #3b3b3c;
    --card: #1f1f20;
    --card-edge: #2a2a2b;
    --gold: #c9a24a;
    --gold-light: #e2c277;
    --text-soft: #d4d4d4;
    --text-muted: #b9b9b9;
    --accent-red: #b3141c;
    --emboss: #161617;
    --emboss-light: #2c2c2d;
  }
  * { box-sizing: border-box; margin: 0; padding: 0; }
  html, body { width: 1200px; height: 799px; overflow: hidden; }
  body {
    background: var(--backdrop);
    font-family: "Montserrat", Arial, sans-serif;
    position: relative;
  }
  .card {
    position: absolute;
    top: 251px;
    width: 520px;
    height: 297px;
    background: var(--card);
    border: 1px solid var(--card-edge);
    box-shadow: 0 14px 30px rgba(0,0,0,.45);
    overflow: hidden;
  }
  .card--front { left: 50px; }
  .card--back { left: 630px; }

  .crest-decoration {
    position: absolute;
    background: radial-gradient(ellipse at 50% 50%, var(--emboss-light) 0%, var(--emboss) 70%, transparent 100%);
    border-radius: 8px;
  }
  .card--front .crest-decoration { left: 0; top: 0; width: 230px; height: 297px; }
  .card--back .crest-decoration { right: 0; top: 50px; width: 220px; height: 247px; }

  .brand-name {
    position: absolute;
    left: 250px;
    top: 128px;
    font-family: "Cinzel", Georgia, serif;
    font-weight: 700;
    font-size: 34px;
    letter-spacing: 1px;
    color: var(--gold);
    white-space: nowrap;
  }

  .person {
    position: absolute;
    left: 40px;
    top: 58px;
  }
  .person__name {
    font-family: "Cinzel", Georgia, serif;
    font-weight: 700;
    font-size: 26px;
    letter-spacing: 1px;
    color: var(--gold);
  }
  .person__role {
    font-size: 15px;
    color: var(--text-muted);
    margin-top: 2px;
  }
  .person__rule {
    width: 46px;
    height: 3px;
    background: var(--accent-red);
    margin-top: 8px;
  }
  .contact {
    position: absolute;
    left: 40px;
    top: 155px;
    list-style: none;
  }
  .contact__item {
    display: flex;
    align-items: center;
    gap: 10px;
    font-size: 13px;
    color: var(--text-soft);
    height: 22px;
  }
  .contact__icon { width: 12px; height: 12px; flex: none; }
</style>
</head>
<body>

<section class="card card--front">
  <div class="crest-decoration" role="img" aria-label="Faint embossed crest decoration"></div>
  <div class="brand-name">Velvet Coach</div>
</section>

<section class="card card--back">
  <div class="person">
    <div class="person__name">DANIEL HART</div>
    <div class="person__role">Founder &amp; CEO</div>
    <div class="person__rule"></div>
  </div>

  <ul class="contact">
    <li class="contact__item">
      <svg class="contact__icon" viewBox="0 0 24 24"><path fill="#c9a24a" d="M6.6 10.8a15 15 0 0 0 6.6 6.6l2.2-2.2a1 1 0 0 1 1-.25 11.4 11.4 0 0 0 3.6.57 1 1 0 0 1 1 1V20a1 1 0 0 1-1 1A17 17 0 0 1 3 4a1 1 0 0 1 1-1h3.5a1 1 0 0 1 1 1c0 1.25.2 2.45.57 3.57a1 1 0 0 1-.25 1z"/></svg>
      416-383-RIDE (416-383-7433)
    </li>
    <li class="contact__item">
      <svg class="contact__icon" viewBox="0 0 24 24"><path fill="#c9a24a" d="M6.6 10.8a15 15 0 0 0 6.6 6.6l2.2-2.2a1 1 0 0 1 1-.25 11.4 11.4 0 0 0 3.6.57 1 1 0 0 1 1 1V20a1 1 0 0 1-1 1A17 17 0 0 1 3 4a1 1 0 0 1 1-1h3.5a1 1 0 0 1 1 1c0 1.25.2 2.45.57 3.57a1 1 0 0 1-.25 1z"/></svg>
      Toll-Free: 1 (888) 294-RIDE (7433)
    </li>
    <li class="contact__item">
      <svg class="contact__icon" viewBox="0 0 24 24"><rect x="2" y="5" width="20" height="14" rx="1" fill="#c9a24a"/><path d="M2 6l10 7 10-7" fill="none" stroke="#1f1f20" stroke-width="2"/></svg>
      book@velvet-coach.com
    </li>
    <li class="contact__item">
      <svg class="contact__icon" viewBox="0 0 24 24"><circle cx="12" cy="12" r="10" fill="none" stroke="#c9a24a" stroke-width="2.5"/><path d="M2 12h20M12 2c3 3 3 17 0 20M12 2c-3 3-3 17 0 20" fill="none" stroke="#c9a24a" stroke-width="2"/></svg>
      velvet-coach.com
    </li>
  </ul>

  <div class="crest-decoration" role="img" aria-label="Faint embossed crest decoration"></div>
</section>

</body>
</html>
```